Modern card design needed for building development company

We are looking for a sharp modern new look for our business cards.
We are a New Zealand based company called TKV Ventures NZ LTD that specialises in subdividing large sections, housing and commercial buildings.
We have attached a photo of the current logo and would like to see it improved somehow as it looks a bit dated.
We are open to any colours.

Target Market(s)

Investors, Property buyers

Industry/Entity Type

Investment

Contact Information for Business Card

TKV VENTURES NZ LTD
www.tkvventuresnz.co.nz

Howard Pennick
Phone +64 21 843 192
Email hdpennick@fernmail.co.nz

Font styles to use
Serif
Sans Serif

Colors
0792cd
33a6d7
85cae6
6b449b
886aae
f04a50
ec1f27
f37122
f68d4d

Requirements
Must have
• Please try and make the logo more modern or if you have a similar one we would like to see it.

```html
<!DOCTYPE html>
<html lang="en">
<head>
<meta charset="utf-8">
<title>TKV Ventures NZ LTD – Business Card</title>
<link rel="stylesheet" href="https://fonts.googleapis.com/css2?family=Tinos&display=swap">
<style>
  :root {
    --purple: #6b449b;
    --purple-soft: #886aae;
    --card: #f0f1f2;
    --backdrop: #e4e4e6;
    --white: #ffffff;
  }
  * { margin: 0; padding: 0; box-sizing: border-box; }
  html, body {
    width: 1200px; height: 724px; overflow: hidden;
    background: var(--backdrop);
    font-family: "Tinos", "Times New Roman", serif;
  }
  .canvas { position: relative; width: 1200px; height: 724px; }
  .card {
    position: absolute; left: 382px; width: 435px; height: 249px;
    background: var(--card); overflow: hidden;
    box-shadow: 0 3px 8px rgba(0,0,0,0.18);
  }
  .card--front { top: 83px; }
  .card--back { top: 416px; }
  .band { position: absolute; left: 0; width: 100%; background: var(--purple); }
  .card--front .band--top { top: 0; height: 24px; }
  .brand-mark {
    position: absolute; left: 178px; top: 52px; width: 80px; height: 80px;
    background: var(--purple-soft);
  }
  .company-name {
    position: absolute; left: 0; right: 0; top: 190px;
    text-align: center; font-size: 24px; color: var(--purple); letter-spacing: 0.2px;
  }
  .company-rule { position: absolute; left: 20px; top: 225px; width: 396px; height: 4px; }
  .card--back .band--top { top: 0; height: 31px; }
  .card--back .band--bottom { bottom: 0; height: 25px; }
  .person-name {
    position: absolute; left: 0; top: 110px; width: 164px; height: 32px;
    background: var(--purple); color: var(--white);
    font-size: 16.5px; line-height: 32px; padding-left: 4px; white-space: nowrap;
  }
  .contact-strip {
    position: absolute; left: 192px; top: 110px; width: 33px; height: 139px;
    background: var(--purple);
  }
  .contact-icon { position: absolute; left: 197px; width: 24px; height: 24px; }
  .contact-text {
    position: absolute; left: 239px; font-size: 13px; color: var(--purple); white-space: nowrap;
  }
</style>
</head>
<body>
<main class="canvas">
  <section class="card card--front">
    <div class="band band--top"></div>
    <div class="brand-mark"></div>
    <h1 class="company-name">TKV VENTURES NZ LTD</h1>
    <svg class="company-rule" viewBox="0 0 396 4" preserveAspectRatio="none" aria-hidden="true">
      <path d="M0 2 Q198 0 396 2 Q198 4 0 2 Z" fill="var(--purple)"/>
    </svg>
  </section>

  <section class="card card--back">
    <div class="band band--top"></div>
    <div class="person-name">HOWARD PENNICK</div>
    <div class="contact-strip"></div>

    <svg class="contact-icon" style="top:125px" viewBox="0 0 24 24" aria-hidden="true">
      <circle cx="12" cy="12" r="10" fill="none" stroke="#fff" stroke-width="1.4"/>
      <path d="M9 15 Q10 11 14 9" fill="none" stroke="#fff" stroke-width="2" stroke-linecap="round"/>
    </svg>
    <svg class="contact-icon" style="top:159px" viewBox="0 0 24 24" aria-hidden="true">
      <circle cx="12" cy="12" r="10" fill="none" stroke="#fff" stroke-width="1.4"/>
      <rect x="7" y="8.5" width="10" height="7" fill="none" stroke="#fff" stroke-width="1.3"/>
      <path d="M7 8.5 L12 12.5 L17 8.5" fill="none" stroke="#fff" stroke-width="1.3"/>
    </svg>
    <svg class="contact-icon" style="top:194px" viewBox="0 0 24 24" aria-hidden="true">
      <g fill="none" stroke="#fff" stroke-width="1.3">
        <circle cx="12" cy="12" r="10"/>
        <ellipse cx="12" cy="12" rx="4.5" ry="10"/>
        <path d="M2 12 H22 M4 7 H20 M4 17 H20 M12 2 V22"/>
      </g>
    </svg>

    <div class="contact-text" style="top:128px">+64 21 843 192</div>
    <div class="contact-text" style="top:162px">hdpennick@fernmail.co.nz</div>
    <div class="contact-text" style="top:197px">www.tkvventuresnz.co.nz</div>

    <div class="band band--bottom"></div>
  </section>
</main>
</body>
</html>
```